Business Card Design Project 4 Construction Business

I am after a creative, but sleek and simple/ clean business card design. This design will form the basis of future items and might include a logo or simply a creative way to lay out the text of my company name 'kestrel ventures'
I like the simplicity of black and white however I would also be happy to see a splash of colour introduced somehow to give the text some interest and make it stand out.
I would like a double sided card.
I am young (ish!) and professional, offering construction and project management services, what I don't want is the traditional builders type card featuring a cheesy hammer/ saw image etc.
As the company name, kestrel ventures, suggests, we focus on working closely and collaboratively together, in synergy with all stakeholders involved in the projects that we undertake
Construction

```html
<!DOCTYPE html>
<html lang="en">
<head>
<meta charset="utf-8">
<title>Kestrel Ventures – Business Card</title>
<link href="https://fonts.googleapis.com/css2?family=Source+Sans+3:wght@400;600;700&display=swap" rel="stylesheet">
<style>
  :root {
    --brand-blue: #1a75bc;
    --brand-blue-soft: #cfe2f2;
    --card-white: #ffffff;
    --backdrop: #e6e7e8;
    --text-grey: #555a5f;
    --name-blue: #1a6fb5;
  }
  * { margin: 0; padding: 0; box-sizing: border-box; }
  html, body {
    width: 1200px;
    height: 508px;
    overflow: hidden;
    background: var(--backdrop);
    font-family: "Source Sans 3", sans-serif;
  }
  .canvas {
    position: relative;
    width: 1200px;
    height: 508px;
  }
  .card {
    position: absolute;
    top: 73px;
    width: 415px;
    height: 236px;
    background: var(--card-white);
    overflow: hidden;
  }
  .card--front { left: 138px; }
  .card--back { left: 659px; }

  /* Front */
  .front__graphic {
    position: absolute;
    left: 0;
    top: 0;
    width: 210px;
    height: 80px;
    background: linear-gradient(170deg, var(--brand-blue-soft) 0%, var(--card-white) 100%);
  }
  .front__panel {
    position: absolute;
    left: 210px;
    top: 0;
    width: 205px;
    height: 236px;
    background: var(--brand-blue);
  }
  .wordmark {
    font-weight: 600;
    text-transform: uppercase;
    line-height: 1;
    white-space: nowrap;
  }
  .wordmark__primary {
    display: block;
    font-size: 32px;
    letter-spacing: 3px;
  }
  .wordmark__secondary {
    display: block;
    font-size: 14px;
    letter-spacing: 9px;
    margin-top: 8px;
  }
  .front__wordmark {
    position: absolute;
    left: 18px;
    top: 64px;
    color: var(--card-white);
  }
  .front__web {
    position: absolute;
    left: 11px;
    top: 212px;
    font-size: 13px;
    color: var(--brand-blue);
  }

  /* Back */
  .back__wordmark {
    position: absolute;
    right: 13px;
    top: 40px;
    text-align: right;
    color: var(--brand-blue);
  }
  .back__wordmark .wordmark__primary { font-size: 40px; letter-spacing: 4px; margin-right: -4px; }
  .back__wordmark .wordmark__secondary { font-size: 17px; letter-spacing: 12px; margin-top: 8px; margin-right: -12px; }
  .contact {
    position: absolute;
    left: 18px;
    top: 106px;
    color: var(--text-grey);
  }
  .contact__name {
    font-size: 18px;
    font-weight: 700;
    color: var(--name-blue);
    line-height: 1.2;
  }
  .contact__role {
    font-size: 16px;
    line-height: 1.3;
  }
  .contact__details {
    list-style: none;
    margin-top: 12px;
    font-size: 13px;
    line-height: 13px;
  }
</style>
</head>
<body>
<main class="canvas">
  <section class="card card--front" aria-label="Card front">
    <div class="front__graphic" role="img" aria-label="Decorative blue swoosh graphic"></div>
    <div class="front__panel">
      <div class="wordmark front__wordmark">
        <span class="wordmark__primary">Kestrel</span>
        <span class="wordmark__secondary">Ventures</span>
      </div>
    </div>
    <p class="front__web">www.kestrelventuresgroup.com.au</p>
  </section>

  <section class="card card--back" aria-label="Card back">
    <div class="wordmark back__wordmark">
      <span class="wordmark__primary">Kestrel</span>
      <span class="wordmark__secondary">Ventures</span>
    </div>
    <div class="contact">
      <p class="contact__name">Owen Tallis</p>
      <p class="contact__role">Director</p>
      <ul class="contact__details">
        <li>0400 555 019</li>
        <li>14 Harlow St Eastwick NSW 2070</li>
        <li>owen@kestrelventuresgroup.com.au</li>
        <li>www.kestrelventuresgroup.com.au</li>
      </ul>
    </div>
  </section>
</main>
</body>
</html>
```